Classic/Royal 5 Items Black coloured Stationery Design

Hello,
I'm looking for an Elegant Stationery set consists of 5 items as the following,
1- Letterhead
2- Business Card
3- Invoice
4- CD/DVD with their Envelope Design
5- Envelope
To let the project move ahead easily, I've included a folder consists many designs I liked from various design sites and it consists of,
1- Business card
2- Corporate Identity
3- Invoice
4- Miscellanies
Inside the first three folders, you will find a folder named "Recommended", it contains designs that I like so much and hoping to have a design like them.
The "Miscellanies" folder got some designs for Inspiration.
I'm waiting for some greats designs, a joomla template designer is a bonus for me as I will need him to design the website layer soon.
Due to upload problems at ArtHerdly, I've uploaded the folder in a .rar archive at multiple site and here is the link http://zup.qx/TRALVBNE .
Thank you
Update :- You can use this alternative download link from my Google drive to download the designs
https://files.plomwex.net/file/d/7Kq2ZpR4m8sVxT1nLw9cYb3HfJd5

```html
<!DOCTYPE html>
<html lang="en">
<head>
<meta charset="utf-8">
<title>Lumen Stay – CD Sleeve and Disc</title>
<link rel="stylesheet" href="https://fonts.googleapis.com/css2?family=Playfair+Display:wght@500&family=Poppins:wght@300&display=swap">
<style>
  :root {
    --page-bg: #ffffff;
    --sleeve-black: #222222;
    --sleeve-black-light: #2a2a2a;
    --disc-black: #232323;
    --disc-black-light: #2c2c2c;
    --rim-silver: #d9d9d9;
    --hub-silver: #cfcfcf;
    --hub-light: #eeeeee;
    --mark-silver: #b5b5b5;
    --tagline-grey: #cfcfcf;
    --watermark-grey: #3b3b3b;
  }
  html, body {
    margin: 0;
    padding: 0;
    width: 1200px;
    height: 957px;
    overflow: hidden;
    background: var(--page-bg);
  }
  .canvas {
    position: relative;
    width: 1200px;
    height: 957px;
  }
  .artwork {
    position: absolute;
    inset: 0;
  }
  .brand-name {
    font-family: "Playfair Display", Georgia, serif;
    font-weight: 500;
    fill: var(--mark-silver);
  }
  .brand-watermark {
    font-family: "Playfair Display", Georgia, serif;
    font-weight: 500;
    fill: var(--watermark-grey);
  }
  .brand-tagline {
    font-family: "Poppins", Arial, sans-serif;
    font-weight: 300;
    fill: var(--tagline-grey);
  }
  .brand-square {
    fill: none;
    stroke: var(--mark-silver);
    stroke-width: 2;
  }
</style>
</head>
<body>
<main class="canvas">
  <svg class="artwork" width="1200" height="957" viewBox="0 0 1200 957" xmlns="http://www.w3.org/2000/svg">
    <defs>
      <radialGradient id="hub-gradient" cx="50%" cy="50%" r="50%">
        <stop offset="0%" stop-color="var(--hub-light)"/>
        <stop offset="100%" stop-color="var(--hub-silver)"/>
      </radialGradient>
      <linearGradient id="sleeve-gradient" x1="0" y1="0" x2="1" y2="1">
        <stop offset="0%" stop-color="var(--sleeve-black)"/>
        <stop offset="55%" stop-color="var(--sleeve-black-light)"/>
        <stop offset="100%" stop-color="var(--sleeve-black)"/>
      </linearGradient>
      <linearGradient id="disc-gradient" x1="0" y1="0" x2="1" y2="1">
        <stop offset="0%" stop-color="var(--disc-black)"/>
        <stop offset="50%" stop-color="var(--disc-black-light)"/>
        <stop offset="100%" stop-color="var(--disc-black)"/>
      </linearGradient>
      <clipPath id="sleeve-clip">
        <path d="M20 208 H617 V415 A50 50 0 0 0 617 515 V773 H20 Z"/>
      </clipPath>
      <clipPath id="disc-clip">
        <circle cx="915" cy="488" r="260"/>
      </clipPath>
    </defs>

    <!-- CD sleeve -->
    <g class="cd-sleeve">
      <path d="M20 208 H617 V415 A50 50 0 0 0 617 515 V773 H20 Z" fill="url(#sleeve-gradient)"/>
      <g class="sleeve-watermark" clip-path="url(#sleeve-clip)">
        <text class="brand-watermark" x="400" y="520" font-size="190" text-anchor="middle">Lumen</text>
        <text class="brand-watermark" x="410" y="755" font-size="210" text-anchor="middle">Stay</text>
      </g>
      <rect class="brand-square" x="299" y="296" width="72" height="90"/>
      <text class="brand-name" x="334" y="432" font-size="38" text-anchor="middle">Lumen Stay</text>
      <text class="brand-tagline" x="329" y="457" font-size="15" text-anchor="middle">Hotels and General Supplies</text>
    </g>

    <!-- CD disc -->
    <g class="cd-disc">
      <circle cx="915" cy="488" r="266" fill="var(--rim-silver)"/>
      <circle cx="915" cy="488" r="260" fill="url(#disc-gradient)"/>
      <g class="disc-watermark" clip-path="url(#disc-clip)">
        <text class="brand-watermark" x="960" y="495" font-size="140" text-anchor="middle">Lumen</text>
        <text class="brand-watermark" x="965" y="680" font-size="160" text-anchor="middle">Stay</text>
      </g>
      <rect class="brand-square" x="881" y="266" width="60" height="74"/>
      <text class="brand-name" x="911" y="378" font-size="30" text-anchor="middle">Lumen Stay</text>
      <text class="brand-tagline" x="909" y="399" font-size="13" text-anchor="middle">Hotels and General Supplies</text>
      <circle cx="915" cy="488" r="72" fill="url(#hub-gradient)"/>
      <circle cx="915" cy="488" r="36" fill="none" stroke="#e6e6e6" stroke-width="6"/>
      <circle cx="915" cy="488" r="26" fill="var(--page-bg)"/>
    </g>
  </svg>
</main>
</body>
</html>
```